Corrigan Architecture (business card)

We need a business card design. We are a full service architectural firm that specializes in mostly residential projects and some commercial projects. We are located in Hudson Valley, New York. We work with high end clients and want a business card that is memorable and has a sleek, modern, design but will not go out of style (timeless).

Target Market(s)

high end residential clients

Industry/Entity Type

Architect

Contact Information for Business Card

Front of card
Company Logo
website: www.corriganarchitectur.example
what we do: residential, Commercial

back of card
Owner's Name: Dorian Corrigan
owner's title: Principal
Business address: 2873 Route 92 Suite A, Brellfordton, NY 12688
phone number: 845-608-2917
e-mail: dc@corriganarchitecture.example

We like:
icons
sleek and clean design
simple not too busy or too much text

Font styles to use
Sans Serif

Colors
0356a4

Requirements
Must have
• company colors are navy blue, white, and gray
• Front of card
• Company Logo
• website: www.corriganarchitectur.example
• what we do: residential, Commercial
• back of card
• Owner's Name: Dorian Corrigan
• owner's title: Principal
• Business address: 2873 Route 92 Suite A, Brellfordton, NY 12688
• phone number: 845-608-2917
• e-mail: dc@corriganarchitecture.example
Nice to have
• We like:
• icons
• sleek and clean design
• simple not too much text
• color of the card to be either blue or gray
Should not have
• we do not like houses in the design or plans of houses-this is over done and we don't like it.
• no QR CODES

```html
<!DOCTYPE html>
<html lang="en">
<head>
<meta charset="utf-8">
<title>Corrigan Architecture – Business Card</title>
<link href="https://fonts.googleapis.com/css2?family=Roboto:wght@300;400;500;700&display=swap" rel="stylesheet">
<style>
  :root {
    --page-bg: #c9cacb;
    --card-gray-top: #575757;
    --card-gray-bottom: #727272;
    --card-white: #ffffff;
    --card-white-shade: #ededed;
    --navy: #27286b;
    --ink: #3a3a3a;
    --muted: #6b6b6b;
    --rule: #9a9a9a;
    --light-text: #e4e4e4;
    --soft-text: #c3c3c3;
  }
  * { box-sizing: border-box; margin: 0; padding: 0; }
  html, body {
    width: 1200px; height: 900px; overflow: hidden;
    background: var(--page-bg);
    font-family: "Roboto", Arial, sans-serif;
  }
  .sheet {
    width: 1200px; height: 900px;
    display: flex; flex-direction: column; align-items: center; justify-content: center;
    gap: 40px;
  }
  .card {
    width: 640px; height: 366px;
    position: relative;
    box-shadow: 0 6px 18px rgba(0,0,0,0.22);
  }

  /* Front */
  .card-front {
    background: linear-gradient(160deg, var(--card-gray-top), var(--card-gray-bottom));
    color: var(--light-text);
    display: flex; flex-direction: column; align-items: center;
    padding-top: 104px;
  }
  .front-name {
    font-weight: 300; font-size: 38px; letter-spacing: 3px;
    text-transform: uppercase; color: var(--light-text);
    display: flex; align-items: center; gap: 14px;
  }
  .front-name .mark-square {
    width: 22px; height: 22px; background: var(--light-text);
  }
  .tagline {
    margin-top: 18px; font-size: 15px; font-weight: 400;
    color: var(--soft-text); letter-spacing: 0.5px;
  }
  .tagline .dot { margin: 0 4px; color: var(--light-text); }
  .website {
    position: absolute; bottom: 44px; left: 0; right: 0; text-align: center;
    font-size: 17px; color: var(--light-text); letter-spacing: 0.4px;
  }
  .website strong { font-weight: 700; }

  /* Back */
  .card-back {
    background: linear-gradient(180deg, var(--card-white) 55%, var(--card-white-shade));
    color: var(--ink);
  }
  .brand {
    position: absolute; left: 44px; top: 120px;
    font-weight: 300; font-size: 22px; line-height: 1.15;
    text-transform: uppercase; letter-spacing: 1.5px; color: var(--navy);
    display: flex; align-items: center; gap: 12px;
  }
  .brand .mark-square { width: 16px; height: 16px; background: var(--navy); flex: none; }
  .divider {
    position: absolute; left: 318px; top: 96px; width: 1px; height: 108px;
    background: var(--rule);
  }
  .contact { position: absolute; left: 346px; top: 92px; }
  .person-name { font-size: 21px; font-weight: 700; color: var(--navy); }
  .person-title { font-size: 15px; color: var(--muted); margin-top: 2px; }
  .contact-list { list-style: none; margin-top: 16px; }
  .contact-list li {
    display: flex; align-items: center; gap: 9px;
    font-size: 14.5px; color: var(--ink); margin-bottom: 6px;
  }
  .contact-list svg { width: 13px; height: 13px; fill: var(--navy); flex: none; }
  .address {
    position: absolute; left: 0; right: 0; bottom: 58px; text-align: center;
    font-size: 15.5px; color: var(--ink);
  }
</style>
</head>
<body>
<main class="sheet">
  <section class="card card-front" aria-label="Card front">
    <div class="front-name"><span class="mark-square"></span>Corrigan</div>
    <p class="tagline">Residential<span class="dot">•</span>Commercial</p>
    <p class="website">www.<strong>corriganarchitectur</strong>.example</p>
  </section>

  <section class="card card-back" aria-label="Card back">
    <div class="brand"><span class="mark-square"></span><span>Corrigan<br>Architecture</span></div>
    <div class="divider"></div>
    <div class="contact">
      <p class="person-name">Dorian Corrigan</p>
      <p class="person-title">Principal</p>
      <ul class="contact-list">
        <li>
          <svg viewBox="0 0 24 24" aria-hidden="true"><path d="M6.6 10.8a15.1 15.1 0 0 0 6.6 6.6l2.2-2.2a1 1 0 0 1 1-.25 11.4 11.4 0 0 0 3.6.57 1 1 0 0 1 1 1V20a1 1 0 0 1-1 1A17 17 0 0 1 3 4a1 1 0 0 1 1-1h3.5a1 1 0 0 1 1 1c0 1.25.2 2.45.57 3.57a1 1 0 0 1-.25 1z"/></svg>
          845-608-2917
        </li>
        <li>
          <svg viewBox="0 0 24 24" aria-hidden="true"><path d="M2 5h20v14H2zm2 2v.5l8 5 8-5V7zm0 2.8V17h16V9.8l-8 5z"/></svg>
          dc@corriganarchitecture.example
        </li>
      </ul>
    </div>
    <p class="address">2873 Route 92 Suite A, Brellfordton, NY 12688</p>
  </section>
</main>
</body>
</html>
```